Luxury Real Estate Website, Midwest, United States

We need web design services for a luxury website. We need IDX Integration with our MLS. We want this to be a very simple website with amazing graphics. We want it to link up with our MailChimp account in order to generate leads through a "More Information" Pop up on the main page. We want the main page to be covered with one large graphic that is a rolling slideshow of active listings of $400,000 and up from the IDX Integration. We need this website to give a very exclusive and sleek look. Lots of black is good... I will upload our logos in Black and Silver. We will also need an "About" page that we are going to call "ZenPO Info". We want our graphics to be extremely impressive. Keep in mind, we are a company in the Midwest of the United States, and our real estate has a different look than homes in California or Florida. We need graphics that are realistic for the Midwest, yet still high-end.
Target Market(s)
Luxury Homeowners in the Midwest United States. The graphics needs to be pristine.
Industry/Entity Type
Real Estate
Coding
Coded - Design and coding required
Number of Pages Required
3 page
Requirements
Must have
- Large graphics with IDX Integration. The photos of real estate need to represent real estate that is common in the Midwest, United States. We also need MailChimp integration. We need a pop up that is titled "My Free Market Analysis" that makes them fill out a contact form asking for Full Name, Email Address, Phone Number and Address. This needs to be a pop up on the front page and will integrate with our MailChimp account. We also need a page called "About Zen PO Home". And another page where clients can download informational PDFs. The main component needs to be a front page search engine connected with the IDX to access active listings from our MLS. I attached our logos and a sample front page of a website. I would love for ours to look similar.
Nice to have
- Lake House photos on midwest lakes are a plus.
Should not have
- Should not have clutter. This website needs to be clean, luxurious and exclusive.

```html
<!DOCTYPE html>
<html lang="en">
<head>
<meta charset="utf-8">
<title>Hearthstone Realty Group</title>
<link href="https://fonts.googleapis.com/css2?family=Lato:ital,wght@0,400;0,700;0,900;1,400&display=swap" rel="stylesheet">
<style>
:root{
  --ink:#1b1b1b;
  --text:#3a3a3a;
  --white:#ffffff;
  --accent:#c6d4e6;
  --accent-deep:#b5c7df;
  --card-fade:#f1f2f4;
  --navy:#1e2940;
  --footer:#151515;
  --footer-text:#9a9a9a;
  --footer-head:#d8d8d8;
}
*{box-sizing:border-box;margin:0;padding:0}
html,body{width:1200px;height:2586px;overflow:hidden;background:var(--white)}
body{position:relative;font-family:'Lato',sans-serif;color:var(--ink)}
.abs{position:absolute}

/* header */
.site-header{left:0;top:0;width:1200px;height:108px;background:var(--white)}
.brand{left:76px;top:34px;font-size:30px;font-weight:400;letter-spacing:1px;color:var(--ink);display:flex;align-items:center;gap:12px}
.brand-mark{width:14px;height:14px;background:var(--ink)}
.main-nav{left:521px;top:41px;display:flex;height:31px;align-items:center}
.main-nav a{font-size:13.5px;text-transform:uppercase;color:var(--ink);text-decoration:none;letter-spacing:.3px;padding:0 16px;line-height:31px;margin-right:2px}
.main-nav a.is-active{background:var(--accent);padding:0 18px;margin-right:12px}

/* hero */
.hero{left:0;top:108px;width:1200px;height:552px;background:linear-gradient(180deg,#3d5678 0%,#566176 30%,#6b4b3a 62%,#4b5a2c 86%,#3f6a22 100%)}
.hero-shade{left:0;top:108px;width:1200px;height:552px;background:rgba(0,0,0,.18)}
.hero-title{left:0;top:270px;width:1200px;text-align:center;color:var(--white);font-size:53px;font-weight:700;letter-spacing:.5px}
.hero-sub{left:0;top:338px;width:1200px;text-align:center;color:var(--white);font-size:30px;font-weight:700;line-height:39px}
.btn{display:block;background:var(--accent);color:var(--ink);font-weight:700;text-transform:uppercase;text-align:center;text-decoration:none}
.hero-btn{left:510px;top:450px;width:180px;height:47px;line-height:47px;font-size:14.5px}
.hero-dots{left:506px;top:615px;display:flex;gap:10px}
.hero-dots span{width:38px;height:3px;background:var(--white);opacity:.85}

/* welcome */
.welcome-photo{left:76px;top:715px;width:600px;height:344px;background:linear-gradient(180deg,#2f8ce0 0%,#8fc0ea 40%,#d9dadb 58%,#7b8c5f 82%,#3d6a36 100%)}
.deco-line{width:3px;background:var(--ink)}
.welcome-card{left:497px;top:743px;width:631px;height:374px;background:linear-gradient(110deg,var(--card-fade) 0%,#e6ebf2 55%,var(--accent) 100%);box-shadow:0 4px 14px rgba(0,0,0,.22);padding:36px 31px}
.welcome-kicker{font-size:24px;line-height:26px;text-transform:uppercase}
.welcome-title{font-size:34px;line-height:38px;font-weight:400;text-transform:uppercase;margin-bottom:16px}
.welcome-card p{font-size:14.4px;line-height:25.8px;color:var(--text)}
.welcome-btn{margin-top:24px;width:150px;height:38px;line-height:38px;font-size:14px}

/* featured */
.featured-band{left:0;top:1181px;width:1200px;height:629px;clip-path:polygon(0 40px,1200px 0,1200px 629px,0 595px);background:linear-gradient(180deg,#17233c 0%,#26314a 45%,#4a4b4e 70%,#2c3a2e 100%)}
.featured-title{left:0;top:1250px;width:1200px;text-align:center;color:var(--white);font-size:33px;font-weight:400;letter-spacing:1px}
.property-card{top:1326px;width:331px;height:377px;background:var(--white);padding:8px}
.property-photo{width:315px;height:195px}
.property-card h3{margin:22px 7px 0;font-size:19px;font-weight:400;text-transform:uppercase}
.property-desc{margin:4px 7px 0;font-size:14px;line-height:22px;color:var(--text)}
.property-meta{position:absolute;left:15px;top:310px;font-size:12.5px;line-height:26px;color:var(--ink)}
.property-price{position:absolute;right:28px;top:317px;font-size:23px;font-weight:700}
.slider-arrow{top:1505px}

/* testimonials */
.family-photo{left:524px;top:1845px;width:602px;height:344px;background:linear-gradient(180deg,#4d5e86 0%,#6a7ba0 40%,#8c8e93 65%,#5f8a3f 100%)}
.testimonial-card{left:74px;top:1874px;width:629px;height:374px;background:linear-gradient(110deg,var(--accent) 0%,#e4e9f0 45%,var(--card-fade) 100%);box-shadow:0 4px 14px rgba(0,0,0,.22);padding:32px 44px}
.testimonial-card h2{font-size:33px;font-weight:400;text-transform:uppercase;letter-spacing:.5px;margin-bottom:14px}
.testimonial-quote{font-style:italic;font-size:14.4px;line-height:29px;color:var(--text)}
.testimonial-name{margin-top:10px;font-size:14px;font-weight:700;text-transform:uppercase}
.testimonial-nav{margin-top:30px;display:flex;gap:16px}
.testimonial-nav span{width:30px;height:30px;border:1.5px solid var(--ink);display:flex;align-items:center;justify-content:center}

/* footer */
.site-footer{left:0;top:2301px;width:1200px;height:285px;background:var(--footer)}
.footer-brand{left:76px;top:2386px;font-size:30px;color:#bdbdbd;letter-spacing:1px;display:flex;align-items:center;gap:12px}
.footer-brand .brand-mark{background:#bdbdbd}
.copyright{left:76px;top:2455px;font-size:13px;line-height:25px;color:var(--footer-head)}
.footer-head{font-size:14.5px;font-weight:700;color:var(--footer-head);text-transform:uppercase;letter-spacing:.5px}
.sitemap{left:374px;top:2350px}
.sitemap ul{list-style:none;margin-top:12px}
.sitemap li{font-size:13px;color:var(--footer-text);line-height:31.5px}
.contact{left:615px;top:2350px}
.contact-company{margin-top:14px;font-size:13px;font-weight:700;color:var(--footer-head);text-transform:uppercase}
.contact-row{display:flex;gap:14px;font-size:13px;color:var(--footer-head);line-height:21px;margin-top:9px}
.contact-row svg{flex:none;margin-top:4px}
.subscribe{left:886px;top:2350px}
.subscribe-form{margin-top:15px;display:flex;width:242px;height:38px}
.subscribe-input{flex:1;background:var(--white);font-size:12.5px;color:var(--ink);line-height:38px;padding-left:10px}
.subscribe-go{width:41px;background:var(--accent);font-size:13px;font-weight:700;text-align:center;line-height:38px}
.follow{margin-top:24px}
.social{margin-top:16px;display:flex;gap:20px}
.social span{width:22px;height:22px;border-radius:50%;background:var(--footer-head)}
</style>
</head>
<body>

<header class="site-header abs">
  <div class="brand abs"><span class="brand-mark"></span>HEARTHSTONE</div>
  <nav class="main-nav abs">
    <a class="is-active" href="#">Home</a>
    <a href="#">ZenPO Info</a>
    <a href="#">About Zen PO Home</a>
    <a href="#">Downloads</a>
    <a href="#">Contact Us</a>
  </nav>
</header>

<section>
  <div class="hero abs" role="img" aria-label="Two-storey brick Midwest family home with lawn under a blue sky"></div>
  <div class="hero-shade abs"></div>
  <h1 class="hero-title abs">HEARTHSTONE REALTY GROUP</h1>
  <p class="hero-sub abs">We are a luxury real estate company from<br>Midwest, United states.</p>
  <a class="btn hero-btn abs" href="#">View Properties</a>
  <div class="hero-dots abs"><span></span><span></span><span></span><span></span></div>
</section>

<section>
  <div class="welcome-photo abs" role="img" aria-label="White lakeside house with wraparound porch and green lawn"></div>
  <div class="deco-line abs" style="left:114px;top:784px;height:224px"></div>
  <div class="welcome-card abs">
    <div class="welcome-kicker">Welcome to</div>
    <h2 class="welcome-title">Hearthstone Realty Group</h2>
    <p>Lorem ipsum dolor sit amet, consectetur adipisicing elit, sed do eiusmod tempor incididunt ut labore et doloreasdes magna aliqua. Ut enim ad minim veniam, quis nostrud exercitation ullamco laboris nisi ut aliquip ex ea commodalo consequat. Duis aute irure dolor in reprehenderit in voluptate velit esse cillum dolore eu fugiat nulla pariatur. Excepteur sint occaecat cupidatat non proident, sunt in culpa qui officia deserunt mollit anim id est laborum.</p>
    <a class="btn welcome-btn" href="#">Read More</a>
  </div>
</section>

<section>
  <div class="featured-band abs" role="img" aria-label="Lake at dusk with dark reflective water"></div>
  <h2 class="featured-title abs">FEATURED PROPERTIES</h2>

  <svg class="slider-arrow abs" style="left:20px" width="42" height="24" viewBox="0 0 42 24"><path d="M41 12H3M13 2L2 12l11 10" fill="none" stroke="#fff" stroke-width="2"/></svg>
  <svg class="slider-arrow abs" style="left:1140px" width="42" height="24" viewBox="0 0 42 24"><path d="M1 12h38M29 2l11 10-11 10" fill="none" stroke="#fff" stroke-width="2"/></svg>

  <article class="property-card abs" style="left:76px">
    <div class="property-photo" role="img" aria-label="Large white estate home with autumn trees" style="background:linear-gradient(180deg,#6b8c4a 0%,#c9c6bd 50%,#4a5a2e 100%)"></div>
    <h3>Name Heading</h3>
    <p class="property-desc">Ut enim ad minim veniam, quis nostrud exercitation ullamco..</p>
    <div class="property-meta">Bed : 3 &nbsp;|&nbsp; Bath: 2<br>Area: 1200 Sqft</div>
    <div class="property-price">$152,20,000</div>
  </article>

  <article class="property-card abs" style="left:434px">
    <div class="property-photo" role="img" aria-label="Stone suburban house with landscaped front garden" style="background:linear-gradient(180deg,#4f6b3a 0%,#9a9a92 45%,#5f8f34 100%)"></div>
    <h3>Name Heading</h3>
    <p class="property-desc">Ut enim ad minim veniam, quis nostrud exercitation ullamco..</p>
    <div class="property-meta">Bed : 3 &nbsp;|&nbsp; Bath: 2<br>Area: 1200 Sqft</div>
    <div class="property-price">$152,20,000</div>
  </article>

  <article class="property-card abs" style="left:795px">
    <div class="property-photo" role="img" aria-label="White boathouse on a blue Midwest lake" style="background:linear-gradient(180deg,#3f6f3a 0%,#d8dcdc 45%,#2a6fa5 70%,#1d5586 100%)"></div>
    <h3>Name Heading</h3>
    <p class="property-desc">Ut enim ad minim veniam, quis nostrud exercitation ullamco..</p>
    <div class="property-meta">Bed : 3 &nbsp;|&nbsp; Bath: 2<br>Area: 1200 Sqft</div>
    <div class="property-price">$152,20,000</div>
  </article>
</section>

<section>
  <div class="family-photo abs" role="img" aria-label="Family standing on the lawn in front of their blue-sided home"></div>
  <div class="deco-line abs" style="left:1082px;top:1890px;height:220px"></div>
  <div class="deco-line abs" style="left:1090px;top:1915px;height:180px"></div>
  <div class="testimonial-card abs">
    <h2>Testimonials</h2>
    <p class="testimonial-quote">Lorem ipsum dolor sit amet, consectetur adipisicing elit, sed do eiusmod tempor incididunt ut labore et doloreasdes magna aliqua. Ut enim ad minim veniam, quis nostrud &nbsp;exercitation ullamco laboris nisi ut aliquip ex ea commodalo consequat &nbsp;irure dolor in &nbsp;reprehenderit in voluptate velit esse cillum dolore eu fugiat nulla pariatur xcepteur sint occaecat cupidatat non proident..”</p>
    <div class="testimonial-name">Name Heading</div>
    <div class="testimonial-nav">
      <span><svg width="12" height="16" viewBox="0 0 12 16"><path d="M9 2L3 8l6 6" fill="none" stroke="#1b1b1b" stroke-width="1.8"/></svg></span>
      <span><svg width="12" height="16" viewBox="0 0 12 16"><path d="M3 2l6 6-6 6" fill="none" stroke="#1b1b1b" stroke-width="1.8"/></svg></span>
    </div>
  </div>
</section>

<footer class="site-footer abs">
</footer>
<div class="footer-brand abs"><span class="brand-mark"></span>HEARTHSTONE</div>
<p class="copyright abs">Copyright © 2018 Company Name<br>All Right Reserved</p>

<div class="sitemap abs">
  <div class="footer-head">Site Map</div>
  <ul>
    <li>Home</li>
    <li>ZenPO Info</li>
    <li>About Zen PO Home</li>
    <li>Downloads</li>
    <li>Contact us</li>
  </ul>
</div>

<div class="contact abs">
  <div class="footer-head">Contact Info</div>
  <div class="contact-company">Hearthstone Realty Group</div>
  <div class="contact-row">
    <svg width="11" height="14" viewBox="0 0 11 14"><path d="M5.5 0A5.5 5.5 0 0 0 0 5.5C0 9.5 5.5 14 5.5 14S11 9.5 11 5.5A5.5 5.5 0 0 0 5.5 0zm0 7.6a2.1 2.1 0 1 1 0-4.2 2.1 2.1 0 0 1 0 4.2z" fill="#d8d8d8"/></svg>
    <span>14 Maple Crest Lane,<br>Lakeview City, USA</span>
  </div>
  <div class="contact-row">
    <svg width="13" height="13" viewBox="0 0 13 13"><path d="M3 0l2 3.2-1.3 1.5a8 8 0 0 0 4.6 4.6L9.8 8 13 10l-.8 2.3C11.7 13 10 13 8 12A13 13 0 0 1 1 5C0 3 0 1.3.7.8z" fill="#d8d8d8"/></svg>
    <span>1-800-555-0142</span>
  </div>
  <div class="contact-row">
    <svg width="13" height="11" viewBox="0 0 13 11"><rect width="13" height="11" rx="1" fill="#d8d8d8"/><path d="M0.5 1l6 4.5 6-4.5" fill="none" stroke="#151515" stroke-width="1.3"/></svg>
    <span>hello@hearthstonerealty.com</span>
  </div>
</div>

<div class="subscribe abs">
  <div class="footer-head">Email Subscribe</div>
  <div class="subscribe-form">
    <div class="subscribe-input">Enter Email Address</div>
    <div class="subscribe-go">GO</div>
  </div>
  <div class="footer-head follow">Follow Us</div>
  <div class="social"><span></span><span></span><span></span><span></span><span></span></div>
</div>

</body>
</html>
```